Poster design for the WILLOW WISP magic show.

We need a poster design for our magic show. This isn't your typical 'small town' magic show. Our show features world class magicians from the Velvet Lantern, in Hollywood California. The show is geared toward everyone, it is family friendly - with a little bit of an edge. We want people to see the poster and feel like they are going to have a unique and sophisticated magical experience. We also want individuals and couples to see the poster and feel like it is a show for them and not only for children.
Updates

Target Market(s)

BRT audience, family audience, the age range is anywhere from 5 - 105. Cool people.

Industry/Entity Type

Town

Requirements
Must have
• Our attached .jpg of the magician floating in the air. Poster size 24x36"
Must have text:
The 3rd Annual Albuquerque Conjuring Gala Presents (small type)
Willow Wisp (should be larger type)
November 24th - 25th
Showtimes 3:00PM & 7:30PM Saturday, 2:00PM Sunday
Tickets available at www.DorvaSeats.example For more information contact Dorva Theatre @ 505.555.0147
Nice to have
• A sort of old school/antique feeling to the poster.
Perhaps a theater marquee
Check out www.grovelumen.example - we love the feeling of this site for our poster...
Feel free to adjust the provided .jpg accordingly in regards to color/size/interaction with the rest of the poster
Should not have
• Should not have clowns, bunnies, anything that would make it feel like a 3 year old's magic themed birthday party.

```html
<!DOCTYPE html>
<html lang="en">
<head>
<meta charset="utf-8">
<title>Willow Wisp — Albuquerque Conjuring Gala Poster</title>
<link rel="stylesheet" href="https://fonts.googleapis.com/css2?family=Cherry+Swash:wght@400;700&family=Old+Standard+TT:wght@400;700&display=swap">
<style>
  :root {
    --gold-deep: #6f5608;
    --gold-mid: #a88a14;
    --gold-warm: #c4a534;
    --gold-light: #f3e29a;
    --gold-pale: #fff4c2;
    --sepia-dark: #3e2a10;
    --sepia-mid: #8a6630;
    --sepia-light: #d9b77a;
  }
  html, body {
    margin: 0;
    padding: 0;
    width: 800px;
    height: 1200px;
    overflow: hidden;
    background: var(--gold-deep);
  }
  .poster {
    position: relative;
    width: 800px;
    height: 1200px;
    overflow: hidden;
    background:
      radial-gradient(ellipse 70% 60% at 50% 45%, var(--gold-warm) 0%, var(--gold-mid) 60%, var(--gold-deep) 100%);
  }
  .frame {
    position: absolute;
    inset: 0;
  }
  .gold-text {
    background: linear-gradient(180deg, var(--gold-pale) 0%, var(--gold-light) 45%, #d8bf5a 70%, var(--gold-light) 100%);
    -webkit-background-clip: text;
    background-clip: text;
    color: transparent;
    filter: drop-shadow(1px 2px 1px rgba(60, 40, 0, 0.55));
    white-space: nowrap;
  }
  .presenter {
    position: absolute;
    left: 0;
    right: 0;
    text-align: center;
    font-family: "Cherry Swash", serif;
    font-weight: 700;
  }
  .presenter-year {
    top: 114px;
    font-size: 19px;
    letter-spacing: 0.5px;
  }
  .presenter-name {
    top: 140px;
    font-size: 27px;
    letter-spacing: 0.5px;
  }
  .show-title {
    position: absolute;
    left: 0;
    right: 0;
    top: 180px;
    margin: 0;
    text-align: center;
    font-family: "Cherry Swash", serif;
    font-weight: 700;
    font-size: 80px;
    line-height: 1;
    letter-spacing: 1px;
    transform: scale(0.66, 2.1);
    transform-origin: top center;
  }
  .show-dates {
    position: absolute;
    left: 0;
    right: 0;
    top: 884px;
    text-align: center;
    font-family: "Cherry Swash", serif;
    font-weight: 700;
    font-size: 60px;
    line-height: 1;
    transform: scale(0.82, 1.55);
    transform-origin: top center;
  }
  .show-details {
    position: absolute;
    top: 1000px;
    left: 0;
    right: 0;
    display: flex;
    justify-content: center;
    gap: 34px;
    font-family: "Old Standard TT", serif;
    font-weight: 700;
    font-size: 14.5px;
    line-height: 1.25;
    color: var(--gold-pale);
    text-shadow: 1px 1px 1px rgba(60, 40, 0, 0.6);
  }
  .showtimes { text-align: right; }
  .tickets { text-align: left; }
</style>
</head>
<body>
<main class="poster">
  <svg class="frame" width="800" height="1200" viewBox="0 0 800 1200" xmlns="http://www.w3.org/2000/svg">
    <defs>
      <radialGradient id="photoTone" cx="50%" cy="40%" r="65%">
        <stop offset="0%" stop-color="var(--sepia-light)"/>
        <stop offset="55%" stop-color="var(--sepia-mid)"/>
        <stop offset="100%" stop-color="var(--sepia-dark)"/>
      </radialGradient>
    </defs>

    <g class="border-lines" fill="none" stroke="var(--gold-light)">
      <rect x="14" y="14" width="772" height="1172" stroke-width="3"/>
      <rect x="24" y="24" width="752" height="1152" stroke-width="1.2"/>
      <rect x="62" y="62" width="676" height="1076" rx="18" stroke-width="2"/>
    </g>

    <g class="portrait-ring">
      <ellipse cx="400" cy="638" rx="250" ry="266" fill="none" stroke="var(--gold-light)" stroke-width="2.5"/>
      <ellipse cx="400" cy="638" rx="237" ry="253" fill="none" stroke="#d8bf5a" stroke-width="20" opacity="0.75"/>
      <ellipse cx="400" cy="638" rx="224" ry="240" fill="none" stroke="var(--gold-light)" stroke-width="2.5"/>
    </g>

    <ellipse class="performer-photo" role="img"
      aria-label="Sepia photograph of the magician floating in mid-air on stage, gripping a levitating chair"
      cx="400" cy="638" rx="216" ry="232" fill="url(#photoTone)"/>
  </svg>

  <div class="presenter presenter-year gold-text">The 3rd Annual</div>
  <div class="presenter presenter-name gold-text">Albuquerque Conjuring Gala Presents</div>

  <h1 class="show-title gold-text">WILLOW WISP</h1>

  <div class="show-dates gold-text">November 24th-25th</div>

  <section class="show-details">
    <div class="showtimes">Showtimes<br>3:00PM &amp; 7:30PM<br>Saturday,<br>2:00PM Sunday</div>
    <div class="tickets">Tickets available at<br>www.DorvaSeats.example<br>For more information contact<br>Dorva Theatre @ 505.555.0147</div>
  </section>
</main>
</body>
</html>
```